Business Card Design Project

I need a template business card for a web design / software company called

"Design Tidewell"

we specialize in propelling archaic paper-based processes into the fore of the 21st century with web based solutions, graphical interfaces, graphic design outsourcing, automation software deployments, database design and development, segmentation of data and preservation of data integrity.

http://glossary.wordharbor.net/browse/lanterns
Marlow Lexicon definitions for phenomena

phenomena
/fɪˈnɒmɪnə/
noun
1.
a plural of phenomenon
phenomenon
/fɪˈnɒmɪnən/
noun (pl) -ena (-ɪnə), -enons
1.
anything that can be perceived as an occurrence or fact by the senses
2.
any remarkable occurrence or person
3.
(philosophy)

the object of perception, experience, etc
(in the writings of Vessel) a thing as it appears and is interpreted in perception and reflection, as distinguished from its real nature as a thing-in-itself Compare noumenon
"

I am very open minded here I am letting you take the design and run with it...

good luck

Target Market(s)

Professional companies, small business in western speaking countries in need of collating design capabilities for web pages, web stores, graphic design or software development projects

Industry/Entity Type

Graphic Design

Colors

Designer to choose colors to be used in the design.

Requirements
Must have
• Designed in Adobe Illustrator

```html
<!DOCTYPE html>
<html lang="en">
<head>
<meta charset="utf-8">
<title>Design Tidewell – Business Card</title>
<link rel="stylesheet" href="https://fonts.googleapis.com/css2?family=Jost:wght@300;400&family=Special+Elite&display=swap">
<style>
  :root {
    --stage: #3b3336;
    --card: #0b0b0b;
    --card-edge: #161616;
    --ink: #f2f2f2;
    --accent: #3fe6ea;
    --back-ink: #ffffff;
  }
  html, body {
    margin: 0;
    padding: 0;
    width: 1200px;
    height: 1000px;
    overflow: hidden;
    background: var(--stage);
  }
  .canvas {
    position: relative;
    width: 1200px;
    height: 1000px;
  }
  .card {
    position: absolute;
    width: 700px;
    height: 440px;
    background: linear-gradient(135deg, var(--card) 0%, var(--card-edge) 70%, var(--card) 100%);
    box-shadow: 0 6px 18px rgba(0, 0, 0, 0.45);
  }
  .card--front { left: 60px; top: 60px; z-index: 2; }
  .card--back  { left: 440px; top: 500px; z-index: 1; }

  .brand {
    position: absolute;
    margin: 0;
    font-family: "Jost", "Futura", sans-serif;
    font-weight: 400;
    font-size: 36px;
    line-height: 1;
    letter-spacing: 2px;
    white-space: nowrap;
  }
  .card--front .brand { left: 36px; top: 90px; color: var(--accent); }
  .card--back .brand  { left: 290px; top: 40px; color: var(--back-ink); }

  .contact {
    position: absolute;
    left: 250px;
    top: 172px;
    font-family: "Jost", "Futura", sans-serif;
    font-weight: 300;
    color: var(--ink);
  }
  .address {
    margin: 0;
    font-style: normal;
    font-size: 20px;
    line-height: 26px;
    letter-spacing: 0.5px;
  }
  .phone {
    margin: 22px 0 0 20px;
    font-size: 25px;
    font-weight: 400;
    letter-spacing: 0.5px;
  }
  .email {
    margin: 12px 0 0 20px;
    font-size: 18px;
    letter-spacing: 0.5px;
  }
  .web {
    position: absolute;
    left: 290px;
    top: 392px;
    margin: 0;
    font-family: "Special Elite", "Courier New", monospace;
    font-size: 25px;
    letter-spacing: 1px;
    color: var(--ink);
    white-space: nowrap;
  }
</style>
</head>
<body>
  <main class="canvas">
    <section class="card card--front" aria-label="Business card front">
      <h1 class="brand">Design Tidewell</h1>
      <div class="contact">
        <address class="address">
          john doe<br>
          something road<br>
          something town<br>
          something city
        </address>
        <p class="phone">tel: 0000 000000</p>
        <p class="email">email: info@designtidewell.???</p>
      </div>
      <p class="web">www.designtidewell.???</p>
    </section>

    <section class="card card--back" aria-label="Business card back">
      <p class="brand">Design Tidewell</p>
    </section>
  </main>
</body>
</html>
```